Service company standing banner design

We are an existing company that just updated our logo. We are attending some oportunity summits in the near future and want a new crisp clean look on our three banners that will be placed in the back of our small booth. The summits we are attending are designed to give local companies opportunities on a prokect we have been awarded to construct in their area. These banners should communicate who we are with no questions when people see them. One banner shall list our services. One to list our values and one to state our goals. All these while being appealing to the eye and using picture of nature. Attached are copies of what we are to replace. also the new logo and the original background pictures in the existing banners

```html
<!DOCTYPE html>
<html lang="en">
<head>
<meta charset="utf-8">
<title>Norvale Services – Booth Banners</title>
<link href="https://fonts.googleapis.com/css2?family=Hind:wght@600;700&display=swap" rel="stylesheet">
<style>
  :root {
    --stage: #c8c8c8;
    --brand-blue: #1337c4;
    --brand-orange: #fb6a1c;
    --ink: #161616;
    --wash: rgba(255,255,255,0.28);
  }
  * { box-sizing: border-box; margin: 0; padding: 0; }
  html, body { width: 1200px; height: 738px; overflow: hidden; background: var(--stage); }
  .stage { position: relative; width: 1200px; height: 738px; }
  .banner {
    position: absolute; top: 69px; width: 255px; height: 587px; overflow: hidden;
    font-family: "Hind", sans-serif; color: var(--ink);
  }
  .banner--values-a { left: 50px; }
  .banner--values-b { left: 334px; }
  .banner--services { left: 622px; }
  .banner--goals { left: 905px; }

  .scene { position: absolute; inset: 0; }
  .scene::after { content: ""; position: absolute; inset: 0; background: var(--wash); }
  .scene--autumn { background: linear-gradient(180deg, #d98a4a 0%, #e3a35a 30%, #d8b46e 55%, #c98a62 80%, #c9a690 100%); }
  .scene--river { background: linear-gradient(180deg, #8fa3a0 0%, #5c7360 25%, #586d56 45%, #8fb3b0 65%, #a9bfc0 85%, #b8b6ad 100%); }
  .scene--coast { background: linear-gradient(180deg, #8fcbd6 0%, #a9d6d9 30%, #b8c4b6 50%, #c9b9a6 70%, #b89f8a 100%); }

  .swoosh { position: absolute; inset: 0; width: 100%; height: 100%; }
  .swoosh .blue { fill: var(--brand-blue); }
  .swoosh .orange { fill: var(--brand-orange); }

  .brand {
    position: absolute; top: 50px; right: 16px;
    display: flex; align-items: center; gap: 6px;
    color: var(--brand-blue); font-weight: 700;
  }
  .brand__mark { width: 22px; height: 22px; border-radius: 50%; background: var(--brand-orange); }
  .brand__name { font-size: 18px; line-height: 1; }
  .brand__sub { display: block; font-size: 11px; letter-spacing: 0.9px; margin-top: 2px; }

  .values { position: absolute; top: 180px; left: 22px; list-style: none; }
  .values li {
    display: flex; align-items: center; gap: 8px;
    font-size: 23px; font-weight: 600; height: 43px;
  }
  .values .icon {
    width: 27px; height: 27px; border-radius: 50%; background: var(--brand-orange);
    display: flex; align-items: center; justify-content: center; flex: none;
  }
  .values .icon svg { width: 15px; height: 15px; fill: none; stroke: #fff; stroke-width: 1.6; }

  .services { position: absolute; top: 152px; left: 24px; list-style: none; }
  .services li { font-size: 21px; font-weight: 600; line-height: 31.3px; }

  .goals { position: absolute; top: 130px; left: 10px; right: 10px; text-align: center; font-size: 19px; font-weight: 600; line-height: 25.6px; }
  .goals p + p { margin-top: 28px; }
</style>
</head>
<body>
<main class="stage">

  <!-- Values banner (two instances) -->
  <section class="banner banner--values-a">
    <div class="scene scene--autumn" role="img" aria-label="Autumn forest with orange and yellow foliage and a leaf-covered path"></div>
    <svg class="swoosh" viewBox="0 0 255 587" preserveAspectRatio="none" aria-hidden="true">
      <path class="blue" d="M0 0H85Q30 20 0 75Z"/>
      <path class="orange" d="M85 0H112Q40 40 0 135V75Q30 20 85 0Z"/>
      <path class="blue" d="M255 330V587H25Q195 520 255 330Z"/>
      <path class="orange" d="M255 425V587H55Q215 540 255 425Z"/>
    </svg>
    <div class="brand"><span class="brand__mark"></span><div class="brand__name">Norvale Services<span class="brand__sub">Limited Partnership</span></div></div>
    <ul class="values">
      <li><span class="icon"><svg viewBox="0 0 16 16"><rect x="2" y="5" width="8" height="8"/><rect x="6" y="2" width="8" height="8"/></svg></span>Integrity</li>
      <li><span class="icon"><svg viewBox="0 0 16 16"><circle cx="6.5" cy="6.5" r="4"/><path d="M9.5 9.5L14 14"/></svg></span>Transparency</li>
      <li><span class="icon"><svg viewBox="0 0 16 16"><path d="M1 7L5 4L8 6L11 4L15 7L9 12L7 11Z"/></svg></span>Respect</li>
      <li><span class="icon"><svg viewBox="0 0 16 16"><circle cx="5" cy="5" r="2"/><circle cx="11" cy="5" r="2"/><path d="M2 13V10Q5 7 8 10V13M8 13V10Q11 7 14 10V13"/></svg></span>Trust</li>
    </ul>
  </section>

  <section class="banner banner--values-b">
    <div class="scene scene--autumn" role="img" aria-label="Autumn forest with orange and yellow foliage and a leaf-covered path"></div>
    <svg class="swoosh" viewBox="0 0 255 587" preserveAspectRatio="none" aria-hidden="true">
      <path class="blue" d="M0 0H85Q30 20 0 75Z"/>
      <path class="orange" d="M85 0H112Q40 40 0 135V75Q30 20 85 0Z"/>
      <path class="blue" d="M255 330V587H25Q195 520 255 330Z"/>
      <path class="orange" d="M255 425V587H55Q215 540 255 425Z"/>
    </svg>
    <div class="brand"><span class="brand__mark"></span><div class="brand__name">Norvale Services<span class="brand__sub">Limited Partnership</span></div></div>
    <ul class="values">
      <li><span class="icon"><svg viewBox="0 0 16 16"><rect x="2" y="5" width="8" height="8"/><rect x="6" y="2" width="8" height="8"/></svg></span>Integrity</li>
      <li><span class="icon"><svg viewBox="0 0 16 16"><circle cx="6.5" cy="6.5" r="4"/><path d="M9.5 9.5L14 14"/></svg></span>Transparency</li>
      <li><span class="icon"><svg viewBox="0 0 16 16"><path d="M1 7L5 4L8 6L11 4L15 7L9 12L7 11Z"/></svg></span>Respect</li>
      <li><span class="icon"><svg viewBox="0 0 16 16"><circle cx="5" cy="5" r="2"/><circle cx="11" cy="5" r="2"/><path d="M2 13V10Q5 7 8 10V13M8 13V10Q11 7 14 10V13"/></svg></span>Trust</li>
    </ul>
  </section>

  <!-- Services banner -->
  <section class="banner banner--services">
    <div class="scene scene--river" role="img" aria-label="Mountain valley with evergreen forest and a rushing river over rocks"></div>
    <svg class="swoosh" viewBox="0 0 255 587" preserveAspectRatio="none" aria-hidden="true">
      <path class="blue" d="M0 0H85Q30 20 0 75Z"/>
      <path class="orange" d="M85 0H112Q40 40 0 135V75Q30 20 85 0Z"/>
      <path class="blue" d="M255 270V587H10Q200 500 255 270Z"/>
      <path class="orange" d="M255 360V587H40Q220 520 255 360Z"/>
    </svg>
    <div class="brand" style="top:60px"><span class="brand__mark"></span><div class="brand__name">Norvale Services<span class="brand__sub">Limited Partnership</span></div></div>
    <ul class="services">
      <li>Pipeline Construction</li>
      <li>Road Maintenance</li>
      <li>Pipeline Clearing</li>
      <li>Land Clearing</li>
      <li>Reclamation</li>
      <li>Civil Works</li>
      <li>Mulching</li>
      <li>Logging</li>
    </ul>
  </section>

  <!-- Goals banner -->
  <section class="banner banner--goals">
    <div class="scene scene--coast" role="img" aria-label="Tropical beach with palm trees, dark rocks and calm sea"></div>
    <svg class="swoosh" viewBox="0 0 255 587" preserveAspectRatio="none" aria-hidden="true">
      <path class="blue" d="M0 0H60Q20 30 0 80Z"/>
      <path class="orange" d="M60 0H100Q35 50 0 122V80Q20 30 60 0Z"/>
      <path class="blue" d="M255 270V587H10Q200 500 255 270Z"/>
      <path class="orange" d="M255 360V587H40Q220 520 255 360Z"/>
    </svg>
    <div class="brand" style="top:40px;right:10px"><span class="brand__mark"></span><div class="brand__name">Norvale Services<span class="brand__sub">Limited Partnership</span></div></div>
    <div class="goals">
      <p>To build and grow a<br>strong regional business<br>providing the best<br>quality for our people<br>and clients.</p>
      <p>Honouring the<br>interests of<br>Indigenous people</p>
    </div>
  </section>

</main>
</body>
</html>
```